Verdant Rooms Stationary Set

Verdant Rooms is a bespoke interior design firm set to provide services to VIP clients with elegance and minimalism is the main theme for our stationary set. We require a full stationary set covering A4 letterhead, A4 & A3 envelopes, business cards, USB's, CDs, email signature and any other item the designer sees fit. logo is already designed and finalized, and we require the designer to use it as is without modifying the logo.

Address to be used on letterhead / business cards ...etc shall be as follows:

Phone : +971 2 518 3076
P.O. Box : 318947
Address: Block C&D, Bldg. 27, Court 14, Abu Dhabi, United Arab Emirates
Website: www.verdantrooms.example

Target Market(s)

VIP Clients

Industry/Entity Type

Interior Design

Font styles to use
Other font styles liked:
• something to be unique

Colors

Designer to choose colors to be used in the design.

Requirements
Must have
• Elegant, minimalistic
Nice to have
• Simple yet elegant design having a sharp yet clean cut format
Should not have
• No additional colours, just colours that are used in the logo (silver, black or gold)

```html
<!DOCTYPE html>
<html lang="en">
<head>
<meta charset="utf-8">
<title>Verdant Rooms Stationery</title>
<link href="https://fonts.googleapis.com/css2?family=Cormorant+Garamond:wght@400;500&family=Open+Sans:wght@400;600;700&display=swap" rel="stylesheet">
<style>
  :root {
    --backdrop: #e6e6e4;
    --paper: #ffffff;
    --card-alt: #f1f1f1;
    --ink: #111111;
    --body-text: #3a3a3a;
    --rule: #222222;
    --faint: rgba(0,0,0,0.07);
    --sig-tone: #e4e4e4;
  }
  * { margin: 0; padding: 0; box-sizing: border-box; }
  html, body { width: 1200px; height: 800px; overflow: hidden; background: var(--backdrop); }
  .stage { position: relative; width: 1200px; height: 800px; }

  .letterhead {
    position: absolute; left: 330px; top: 30px; width: 525px; height: 740px;
    background: var(--paper); box-shadow: 0 2px 8px rgba(0,0,0,0.12);
    font-family: "Open Sans", sans-serif; color: var(--body-text);
  }
  .band { position: absolute; display: block; }
  .band--top { right: 0; top: 0; }
  .band--bottom { left: 0; bottom: 0; }

  .brand {
    position: absolute; left: 0; right: 0; top: 78px;
    display: flex; align-items: center; justify-content: center; gap: 16px;
  }
  .brand__rule { width: 100px; height: 1px; background: var(--rule); }
  .brand__name {
    font-family: "Cormorant Garamond", serif; font-weight: 500;
    font-size: 30px; letter-spacing: 2px; color: var(--ink); white-space: nowrap;
  }

  .letter-date { position: absolute; right: 67px; top: 188px; font-size: 7.5px; }

  .letter-body { position: absolute; left: 68px; right: 67px; top: 255px; }
  .letter-body p { font-size: 7.4px; line-height: 17px; margin-bottom: 16px; }

  .backdrop-name {
    position: absolute; left: 0; right: 0; top: 440px; text-align: center;
    font-family: "Cormorant Garamond", serif; font-weight: 500;
    font-size: 48px; letter-spacing: 4px; color: var(--faint);
  }

  .signature { position: absolute; left: 68px; top: 568px; }
  .signature__mark { width: 84px; height: 20px; background: var(--sig-tone); border-radius: 3px; margin-bottom: 4px; }
  .signature__name { font-size: 8px; font-weight: 700; color: var(--ink); line-height: 10px; }
  .signature__role { font-size: 7.5px; line-height: 10px; }

  .contact {
    position: absolute; left: 0; right: 0; top: 686px; text-align: center;
    font-family: "Cormorant Garamond", serif; font-size: 8px; color: var(--ink); line-height: 14px;
  }
  .contact b { font-weight: 500; margin-right: 3px; }
  .website {
    position: absolute; right: 40px; top: 712px;
    font-size: 7.5px; font-weight: 700; color: var(--ink);
  }

  .business-card {
    position: absolute; width: 260px; height: 152px;
    background: var(--paper); box-shadow: 0 2px 6px rgba(0,0,0,0.12);
    display: flex; align-items: center; justify-content: center;
  }
  .business-card--front { left: 900px; top: 60px; }
  .business-card--back { left: 900px; top: 250px; width: 268px; height: 156px; background: var(--card-alt); }
  .business-card .brand__name { font-size: 26px; }
</style>
</head>
<body>
<main class="stage">
  <article class="letterhead">
    <svg class="band band--top" width="374" height="13" viewBox="0 0 374 13">
      <polygon points="0,0 374,0 374,13 13,13" fill="var(--ink)"/>
    </svg>

    <header class="brand">
      <span class="brand__rule"></span>
      <span class="brand__name">Verdant Rooms</span>
      <span class="brand__rule"></span>
    </header>

    <p class="letter-date">Date, 10 September, 2019</p>

    <div class="backdrop-name" aria-hidden="true">Verdant Rooms</div>

    <section class="letter-body">
      <p>This is a sample letter that has been placed to demonstrate typing remat (Your Company). letterhead design. When positioned properly, it will serve to work in harmony with all other elements letterhead. This letterhead design is meant to project an image</p>
      <p>This letterhead design is meant project an image of professionalism reliability. By using simple aligen we have created a very spacious feeling. The simplicity suggest strength the spaciousness contributes to aesthetics the layout. These basic qualities along with the (Your Company)</p>
      <p>look and helps reinforce the (Your Company) brand. letterhead design is meant to project an image p design. When positioned properly, it will serve to work in harmony all the other elements letterhead. sionalism and reliability.</p>
      <p>This letterhead design is based on the (Form of your logo) form (Your Company) logo. Each element we have created a very spacious feeling. The simplicity suggests strength the spaciousness contribute part of the (Form of your logo).</p>
    </section>

    <div class="signature">
      <div class="signature__mark" role="img" aria-label="Handwritten signature of Adam Rowell"></div>
      <p class="signature__name">Adam Rowell</p>
      <p class="signature__role">Manager</p>
    </div>

    <footer class="contact">
      <p><b>E:</b> info@verdantrooms.example &nbsp;&nbsp; <b>P:</b> +971 2 518 3076</p>
      <p>Block C&amp;D, Bldg. 27, Court 14, Abu Dhabi, United Arab Emirates</p>
    </footer>
    <p class="website">www.verdantrooms.example</p>

    <svg class="band band--bottom" width="367" height="13" viewBox="0 0 367 13">
      <polygon points="0,0 354,0 367,13 0,13" fill="var(--ink)"/>
    </svg>
  </article>

  <div class="business-card business-card--front">
    <span class="brand__name">Verdant Rooms</span>
  </div>
  <div class="business-card business-card--back">
    <span class="brand__name">Verdant Rooms</span>
  </div>
</main>
</body>
</html>
```